Business Card for Language School (2 locations)

We need a sleek business card for a language school that is looking to update our image to be more professional. We work with students ages Pre-Kindergarten through adults. Our idea is to have an all-black business card with white or silver lettering. On the front will be the name of our school (Bright Maple English Academy), and on the back there will be information for our location, phone number, email, and website (and possibly social media information). We have two school branches, so the address, phone number, and email address will be different for each branch, but all of the other information will stay the same. We'd like each branch to have a different color card edge that is neon. We are also open to suggestions and new ideas!

Some answers to questions we have received:
1. The reason we haven't added a logo is because we are looking to get a new one. We hadn't originally planned to do that at this time, but we are going to look into updating our project to include that as another aspect of it. We had previously planned to just include the school name on the front without a logo at this time.
2. We currently have two branches of our school, and we want our business card design to be uniform for each location. While it might make sense to put the information on one card right now, we plan to have more locations in the future, so we want to plan ahead with a unified design right now.
3. Our school addresses and phone numbers can be found on our website: www.brightmapleenglish.example (at the bottom of the page)!
Updates

Part of this contest is also a new logo design. Our previous design was a train, which we would be open to keeping if it had an updated, sleeker design.

Contact Information for Business Card

Card #1:
Bright Maple English Academy (Qiaolin Branch)
Yuqing W. Rd. Sec. 3, Lane 412, No. 29, 1F
Beitou District, Taipei City 11268
02-2649-3058
qiaolin@brightmapleenglish.example

Card #2:
Bright Maple English Academy (Fenghe Branch)
Fulan Road, No. 318, 1F
Songshan District, Taipei City 10573
02-2761-4402
fenghe@brightmapleenglish.example

Both cards:
Website: www.brightmapleenglish.example
Facebook: www.facebook.com/brightmapleenglish
Instagram: @brightmapleenglish

```html
<!DOCTYPE html>
<html lang="en">
<head>
<meta charset="utf-8">
<title>Bright Maple English Academy – Business Card</title>
<link href="https://fonts.googleapis.com/css2?family=Noto+Serif:ital,wght@1,500;1,600&display=swap" rel="stylesheet">
<style>
  :root {
    --page-top: #efebe7;
    --page-bottom: #ffffff;
    --card: #1d1b1a;
    --card-light: #2a2826;
    --silver: #ebe8e4;
    --accent: #1a9ad6;
    --dot-social: #5a5f9a;
    --dot-web: #6aa6d6;
    --dot-photo: #c8405e;
  }
  * { margin: 0; padding: 0; box-sizing: border-box; }
  html, body { width: 1200px; height: 1200px; overflow: hidden; }
  body {
    background: linear-gradient(180deg, var(--page-top) 0%, var(--page-bottom) 55%);
    font-family: "Noto Serif", Georgia, serif;
    font-style: italic;
    color: var(--silver);
    position: relative;
  }
  .card {
    position: absolute;
    left: 235px;
    width: 730px;
    height: 437px;
    background: radial-gradient(ellipse at 60% 45%, var(--card-light) 0%, var(--card) 70%);
    box-shadow: 0 2px 6px rgba(0,0,0,.35);
    overflow: hidden;
  }
  .card--front { top: 139px; }
  .card--back { top: 649px; }
  .card__texture { position: absolute; inset: 0; }
  .t { position: absolute; white-space: nowrap; line-height: 1; }
  .center { transform: translateX(-50%); }
  .front-name { font-size: 38px; font-weight: 600; }
  .back-name { font-size: 21px; font-weight: 500; }
  .branch-name { font-size: 27px; font-weight: 600; }
  .social { font-size: 12px; font-weight: 500; }
  .contact { font-size: 16px; font-weight: 500; }
  .dot { position: absolute; width: 25px; height: 25px; border-radius: 50%; }
  .dot--social { background: var(--dot-social); }
  .dot--web { background: var(--dot-web); }
  .dot--photo { background: var(--dot-photo); }
  .icon { position: absolute; }
</style>
</head>
<body>

<section class="card card--front">
  <div class="card__texture" role="img" aria-label="Faint dark low-poly texture"></div>
  <div class="t center front-name" style="left:365px; top:168px;">Bright Maple</div>
  <div class="t center front-name" style="left:365px; top:214px;">English Academy</div>
</section>

<section class="card card--back">
  <div class="card__texture" role="img" aria-label="Faint dark low-poly texture"></div>

  <div class="t center back-name" style="left:130px; top:44px;">Bright Maple</div>
  <div class="t center back-name" style="left:130px; top:71px;">English Academy</div>

  <span class="dot dot--social" style="left:27px; top:163px;"></span>
  <div class="t social" style="left:57px; top:169px;">www.friendpage.example/brightmapleenglish</div>

  <span class="dot dot--web" style="left:27px; top:210px;"></span>
  <div class="t social" style="left:57px; top:216px;">www.brightmapleenglish.example</div>

  <span class="dot dot--photo" style="left:27px; top:251px;"></span>
  <div class="t social" style="left:65px; top:257px;">@brightmapleenglish</div>

  <div class="t center branch-name" style="left:487px; top:121px;">Bright Maple</div>
  <div class="t center branch-name" style="left:487px; top:156px;">English Academy</div>
  <div class="t center branch-name" style="left:487px; top:190px;">(Fenghe Branch)</div>

  <svg class="icon" style="left:289px; top:247px;" width="48" height="40" viewBox="0 0 48 40">
    <path d="M24 2 L46 20 L41 20 L24 7 L7 20 L2 20 Z" fill="var(--accent)"/>
    <path d="M9 19 L24 8 L39 19 L39 39 L29 39 L29 27 L19 27 L19 39 L9 39 Z" fill="var(--accent)"/>
  </svg>
  <div class="t contact" style="left:349px; top:270px;">Fulan Road, No. 318, 1F</div>
  <div class="t contact" style="left:343px; top:306px;">Songshan District, Taipei City 10573</div>

  <svg class="icon" style="left:298px; top:329px;" width="32" height="26" viewBox="0 0 32 26">
    <path d="M1 8 Q16 -2 31 8 L29 12 L22 10 L22 7 Q16 5 10 7 L10 10 L3 12 Z" fill="var(--accent)"/>
    <path d="M7 12 L25 12 L30 25 L2 25 Z" fill="var(--accent)"/>
    <circle cx="16" cy="18" r="4" fill="var(--card)"/>
  </svg>
  <div class="t contact" style="left:338px; top:338px;">02-2761-4402</div>

  <svg class="icon" style="left:297px; top:377px;" width="35" height="20" viewBox="0 0 35 20">
    <rect x="0" y="0" width="35" height="20" fill="var(--accent)"/>
    <path d="M0 0 L17.5 12 L35 0 M0 20 L13 9 M35 20 L22 9" stroke="var(--card)" stroke-width="1.5" fill="none"/>
  </svg>
  <div class="t contact" style="left:341px; top:379px;">fenghe@brightmapleenglish.example</div>
</section>

</body>
</html>
```